Marlowbrook Wines Logo /Bottle Label

We need a contemporary update of our winery logo and wine label.
We are a small family owned vineyard with cellar door sales located at Tarrington in the Henty Wine Region in south west Victoria Australia.
Our existing logo is an illustration of our homestead including vines in front of the homestead. We wish to include a representation of the homestead, but not necessarily the grape vines. Perhaps with a splash of colour. The final design should be conservative, classy and eye catching. The design will be used for a label on our suite of wines, including our first sparkling wine.
Updates
Designers, please note we wish to incorporate a representation of the homestead in the logo/label but not simply by using the photo of the homestead. The logo/label could be a contemporary representation of the homestead by using the outline and architectural features of the homestead in the image.
We have received several designs which fall into the trap of repeating the concept of our existing logo, by simply using the photo or illustration of the homestead provided in the brief.
We wish to encourage designers to come up with a new concept for our label, but for brand continuity we also wish to incorporate a representation of the homestead. It could be a contemporary symbol, rather than the photo or illustration. We prefer not to have trees in the logo, however grape vines may work.
Reason: To all designers, we have extended our deadline by one week as we have received only a limited number of designs and several designers have indicated that they wish to submit designs however due to other commitments have not had time to prepare and submit designs.
Reason: We have now committed to designer payment, and have extended the project for 4 days to give time to designers who were waiting until we committed to payment.
Target Market(s)
Our wines are aimed at the higher end of the market. Our customers are typically middle age and older people who are wine lovers
Industry/Entity Type
Conservative
Requirements
Must have
- - Must have a representation of our homestead see attached photo and illustration, and existing wine bottle label

```html
<!DOCTYPE html>
<html lang="en">
<head>
<meta charset="utf-8">
<title>Marlowbrook Wines – Pinot Noir Label</title>
<link rel="stylesheet" href="https://fonts.googleapis.com/css2?family=Cinzel:wght@400;500&display=swap">
<style>
  :root {
    --page: #ffffff;
    --paper: #dcc8ab;
    --paper-light: #e6d6bd;
    --paper-dark: #cfb897;
    --ink: #231f20;
    --band-text: #ffffff;
    --photo-dark: #3a3a3a;
    --photo-light: #d9d9d9;
  }
  * { margin: 0; padding: 0; box-sizing: border-box; }
  html, body {
    width: 1200px;
    height: 1000px;
    overflow: hidden;
    background: var(--page);
  }
  .canvas {
    position: relative;
    width: 1200px;
    height: 1000px;
  }
  .label {
    position: absolute;
    left: 200px;
    top: 210px;
    width: 800px;
    height: 581px;
    background: radial-gradient(ellipse at 40% 35%, var(--paper-light), var(--paper) 60%, var(--paper-dark));
    overflow: hidden;
    font-family: "Cinzel", "Times New Roman", serif;
    color: var(--ink);
  }
  .wordmark-rule {
    position: absolute;
    top: 86px;
    height: 2px;
    background: var(--ink);
  }
  .wordmark-rule--left { left: 0; width: 108px; }
  .wordmark-rule--right { right: 0; width: 130px; }
  .wordmark {
    position: absolute;
    left: 118px;
    width: 540px;
    top: 46px;
    text-align: center;
    font-size: 54px;
    font-weight: 400;
    letter-spacing: 2px;
    line-height: 1;
    color: var(--ink);
  }
  .homestead-frame {
    position: absolute;
    left: 204px;
    top: 137px;
    width: 418px;
    height: 294px;
  }
  .band-rule {
    position: absolute;
    left: 0;
    width: 800px;
    top: 387px;
    height: 4px;
    background: var(--ink);
  }
  .variety-band {
    position: absolute;
    left: 0;
    top: 403px;
    width: 800px;
    height: 110px;
    background: var(--ink);
    color: var(--band-text);
  }
  .vintage {
    position: absolute;
    left: 300px;
    width: 200px;
    top: 30px;
    text-align: center;
    font-size: 24px;
    font-family: "Times New Roman", serif;
  }
  .variety {
    position: absolute;
    left: 250px;
    width: 300px;
    top: 60px;
    text-align: center;
    font-size: 28px;
    letter-spacing: 1px;
  }
  .volume {
    position: absolute;
    right: 22px;
    top: 68px;
    font-size: 28px;
    font-weight: 500;
  }
  .stripe {
    position: absolute;
    left: 0;
    width: 800px;
    background: var(--ink);
  }
  .stripe--one { top: 526px; height: 6px; }
  .stripe--two { top: 542px; height: 4px; }
  .stripe--three { top: 559px; height: 22px; }
</style>
</head>
<body>
<main class="canvas">
  <section class="label" aria-label="Marlowbrook Wines 2012 Pinot Noir label">
    <div class="wordmark-rule wordmark-rule--left"></div>
    <h1 class="wordmark">Marlowbrook</h1>
    <div class="wordmark-rule wordmark-rule--right"></div>

    <svg class="homestead-frame" viewBox="0 0 418 294" xmlns="http://www.w3.org/2000/svg">
      <defs>
        <linearGradient id="homestead-tone" x1="0" y1="0" x2="0" y2="1">
          <stop offset="0" stop-color="var(--photo-light)"/>
          <stop offset="0.55" stop-color="var(--photo-dark)"/>
          <stop offset="1" stop-color="var(--photo-light)"/>
        </linearGradient>
      </defs>
      <ellipse cx="209" cy="147" rx="206" ry="144" fill="#ffffff" stroke="var(--ink)" stroke-width="5"/>
      <ellipse cx="209" cy="140" rx="192" ry="112" fill="url(#homestead-tone)"
               role="img" aria-label="Black and white engraving-style image of the family homestead with verandah and garden"/>
    </svg>

    <div class="band-rule"></div>
    <div class="variety-band">
      <p class="vintage">2012</p>
      <p class="variety">Pinot Noir</p>
      <p class="volume">750ml</p>
    </div>

    <div class="stripe stripe--one"></div>
    <div class="stripe stripe--two"></div>
    <div class="stripe stripe--three"></div>
  </section>
</main>
</body>
</html>
```